New young doctors office business card

Doctor's office
Hello:
My name is Dr. Mateo Anselmo Quiroga Benítez. I need a business card for my new office located within a hospital. The name of the hospital is "Hospital Almendral". Although the hospital logo and name must be included in the business card, please make me a personal logo for myself. The logo might be maybe my name in a stylish font, or my initials (MAQB) or something like that. Im more inclined to a font logo, rather than a image logo, but a good one might change my mind. The info on my business card is going to be in spanish. The following info must be included please (the info within parenthesis is not to be included, it is provided for you to understand it since it's in spanish, so you can properly place it on the card):
-Dr. Mateo Anselmo Quiroga Benítez (my name)
-Medicina general (My specialty)
-Hospital Almendral (The name of the hospital where my office is)
-Calle Tomás Ibarrola #527 Col. Peñascal (address)
-Tel 471-5836 (Office phone)
-Sábado y domingo 10:00 am a 10:00pm (Office hours)
-Emergencias: 613-907-5148 (Emergency phone)
-mateoqb@correoandino.net (email)
-English Spoken
So, that's all the info i need to be on the business card. Although it's a business card for a doctor's office, i dont want it to be a boring, plain business card. Make it eye-catchy and stylish please. As i said, the hospital logo must be included. You'll find it on the heading of the PDF file i attached, but dont make it the center of attention.
Physician
Hello:My name is Dr. Mateo Anselmo Quiroga Benítez. I need a business card for my new office located within a hospital. The name of the hospital is "Hospital Almendral". Although the hospital logo and name must be included in the business card, please make me a personal logo for myself. The logo might be maybe my name in a stylish font, or my initials (MAQB) or something like that. Im more inclined to a font logo, rather than a image logo, but a good one might change my mind. The info on my business card is going to be in spanish. The following info must be included please (the info within parenthesis is not to be included, it is provided for you to understand it since it's in spanish, so you can properly place it on the card):-Dr. Mateo Anselmo Quiroga Benítez (my name)-Medicina general (My specialty)-Hospital Almendral (The name of the hospital where my office is)-Calle Tomás Ibarrola #527 Col. Peñascal (address)-Tel 471-5836 (Office phone)-Sábado y domingo 10:00 am a 10:00pm (Office hours)-Emergencias: 613-907-5148 (Emergency phone)-mateoqb@correoandino.net (email)-English Spoken So, that's all the info i need to be on the business card. Although it's a business card for a doctor's office, i dont want it to be a boring, plain business card. Make it eye-catchy and stylish please. As i said, the hospital logo must be included. You'll find it on the heading of the PDF file i attached, but dont make it the center of attention.

```html
<!DOCTYPE html>
<html lang="es">
<head>
<meta charset="utf-8">
<title>Tarjeta de presentación — Dr. Mateo Anselmo Quiroga Benítez</title>
<link rel="stylesheet" href="https://fonts.googleapis.com/css2?family=Montserrat:wght@700;800&family=Roboto:wght@400;500;700&display=swap">
<style>
  :root {
    --page: #1c1c1e;
    --card: #0d0d0e;
    --card-edge: #18181a;
    --silver: #b9b9bd;
    --silver-dim: #6d6d72;
    --white: #f4f4f4;
    --red: #d3262c;
    --red-light: #e4343a;
    --red-dark: #a41e22;
    --purple: #9b4fc0;
    --indigo: #3e3f9a;
    --line: #d9d9d9;
  }
  * { box-sizing: border-box; margin: 0; padding: 0; }
  html, body { width: 1200px; height: 1200px; overflow: hidden; }
  body {
    background: var(--page);
    font-family: "Roboto", Arial, sans-serif;
    display: flex; flex-direction: column; align-items: center; justify-content: center;
    gap: 40px;
  }
  .card {
    position: relative; width: 960px; height: 549px;
    background: linear-gradient(135deg, var(--card-edge), var(--card) 60%);
    overflow: hidden;
    box-shadow: 0 18px 40px rgba(0,0,0,0.55);
  }
  .mark {
    font-family: "Roboto", Arial, sans-serif; font-weight: 700;
    letter-spacing: 2px; line-height: 1; white-space: nowrap;
  }

  /* Front */
  .front__identity { position: absolute; left: 90px; top: 175px; }
  .card--front .mark { font-size: 84px; color: var(--silver); }
  .front__name {
    margin-top: 26px; font-family: "Montserrat", Arial, sans-serif; font-weight: 800;
    font-size: 25px; letter-spacing: 1.5px; color: var(--silver); text-transform: uppercase;
    white-space: nowrap;
  }
  .front__specialty {
    margin-top: 4px; font-family: "Montserrat", Arial, sans-serif; font-weight: 700;
    font-size: 16px; letter-spacing: 1px; color: var(--silver-dim); text-transform: uppercase;
  }

  /* Back */
  .back__heading { position: absolute; left: 60px; top: 48px; }
  .back__name { font-size: 30px; font-weight: 500; color: var(--white); letter-spacing: 1px; white-space: nowrap; }
  .back__specialty { font-size: 22px; font-weight: 500; color: var(--red); margin-top: 2px; }
  .card--back .mark { position: absolute; right: 70px; top: 160px; font-size: 78px; color: var(--white); }
  .back__hospital { position: absolute; left: 60px; top: 250px; color: var(--white); }
  .back__hospital-name { font-size: 25px; font-weight: 700; }
  .back__address { font-size: 19px; margin-top: 2px; white-space: nowrap; }
  .back__rule { position: absolute; left: 50px; right: 50px; top: 318px; height: 2px; background: var(--line); }
  .contact { position: absolute; left: 60px; top: 334px; list-style: none; color: var(--white); font-size: 20px; }
  .contact li { display: flex; align-items: center; gap: 12px; height: 30px; white-space: nowrap; }
  .contact svg { width: 20px; height: 20px; flex: none; }
  .contact strong { font-weight: 700; }
  .back__partner {
    position: absolute; right: 70px; top: 400px; width: 78px; height: 72px;
    background: var(--white);
  }
  .band { position: absolute; left: 0; right: 0; bottom: 0; height: 52px; display: flex; }
  .band__lang {
    width: 300px; background: linear-gradient(90deg, var(--purple), var(--indigo));
    color: var(--white); font-size: 20px; display: flex; align-items: center; padding-left: 40px;
    letter-spacing: 1px; white-space: nowrap;
  }
  .band__hours {
    flex: 1; background: linear-gradient(90deg, var(--red-dark), var(--red-light));
    color: var(--white); font-size: 20px; display: flex; align-items: center; justify-content: center;
    letter-spacing: 1px; white-space: nowrap;
  }
  .band__pulse { position: absolute; left: 280px; bottom: 10px; width: 60px; height: 40px; }
</style>
</head>
<body>
  <section class="card card--front">
    <div class="front__identity">
      <p class="mark">MAQB</p>
      <p class="front__name">Dr. Mateo Anselmo Quiroga Benítez</p>
      <p class="front__specialty">Medicina general</p>
    </div>
  </section>

  <section class="card card--back">
    <header class="back__heading">
      <h1 class="back__name">Dr. Mateo Anselmo Quiroga Benítez</h1>
      <p class="back__specialty">Medicina general</p>
    </header>
    <p class="mark">MAQB</p>
    <div class="back__hospital">
      <p class="back__hospital-name">Hospital Almendral</p>
      <p class="back__address">Calle Tomás Ibarrola #527 Col. Peñascal</p>
    </div>
    <div class="back__rule"></div>
    <ul class="contact">
      <li>
        <svg viewBox="0 0 24 24"><path fill="#d3262c" d="M3 9c0-3 4-5 9-5s9 2 9 5l-1 2h-4l-1-2h-6l-1 2H4zM6 12h12l2 7H4z"/></svg>
        <span>Office: 471-5836</span>
      </li>
      <li>
        <svg viewBox="0 0 24 24"><path fill="#d3262c" d="M3 9c0-3 4-5 9-5s9 2 9 5l-1 2h-4l-1-2h-6l-1 2H4zM6 12h12l2 7H4z"/></svg>
        <span><strong>Emergencias: 613-907-5148</strong></span>
      </li>
      <li>
        <svg viewBox="0 0 24 24"><rect x="2" y="5" width="20" height="14" fill="#d3262c"/><path d="M2 5l10 8 10-8" fill="none" stroke="#0d0d0e" stroke-width="2"/></svg>
        <span>mateoqb@correoandino.net</span>
      </li>
    </ul>
    <div class="back__partner" role="img" aria-label="Hospital badge"></div>
    <div class="band">
      <div class="band__lang">ENGLISH SPOKEN</div>
      <div class="band__hours">SÁBADO Y DOMINGO 10:00 AM A 10:00PM</div>
    </div>
    <svg class="band__pulse" viewBox="0 0 60 40"><polyline points="0,32 18,32 24,14 30,38 36,24 42,32 60,32" fill="none" stroke="#ffffff" stroke-width="2"/></svg>
  </section>
</body>
</html>
```